Pitch Deck Redesign

Our company is currently in need of our pitch deck to be revamped and made much cleaner. We have a solid foundation and framework and now just need a final polishing.
We are looking to hire a freelance graphic designer that we can create a long-term relationship with. We want to be able to utilize this person week after week for various projects and designs. Designs will need to be delivered to our team both as png that will slide ride into a wide view powerpoint presentation and will need to supply original design file (PSD).
Thank you in advance for your responses and time,
Milo
It Company

```html
<!DOCTYPE html>
<html lang="en">
<head>
<meta charset="utf-8">
<title>Pontiva Pitch Deck</title>
<link href="https://fonts.googleapis.com/css2?family=Raleway:wght@300;400;700;800&family=Source+Sans+3:wght@400;600;700;800&display=swap" rel="stylesheet">
<style>
:root{
  --page:#e6e6e6;
  --navy:#44546a;
  --sky:#36a9e1;
  --blue:#3a6fc4;
  --yellow:#fbb900;
  --green:#8cc63f;
  --orange:#f07d1a;
  --ink:#222;
  --muted:#666;
  --white:#fff;
}
*{box-sizing:border-box;margin:0;padding:0}
html,body{width:1200px;height:1027px;overflow:hidden;background:var(--page)}
body{font-family:"Source Sans 3",sans-serif;color:var(--ink);position:relative}
.slide{position:absolute;width:588px;height:330px;overflow:hidden;background:var(--white);box-shadow:0 1px 3px rgba(0,0,0,.25)}
.abs{position:absolute}
.center{text-align:center}
.head{font-family:Raleway,sans-serif;font-weight:300;color:var(--ink)}
.head b{font-weight:800}
.underline{border-bottom:2px solid var(--orange);padding-bottom:2px}
.pill{position:absolute;height:21px;border-radius:11px;background:var(--white);display:flex;align-items:center;overflow:hidden;font-size:8px;color:#333}
.pill .globe{width:30px;height:100%;background:var(--sky);display:flex;align-items:center;justify-content:center}
.pill span{flex:1;text-align:center}

/* cover */
.s-cover{left:9px;top:9px}
.cover-left{left:0;top:0;width:308px;height:330px;background:linear-gradient(160deg,#5a4a3c,#2c2a2a 60%,#1d1d22)}
.cover-band{left:308px;top:0;width:16px;height:330px;background:#62b8d8}
.cover-band2{left:324px;top:0;width:17px;height:330px;background:rgba(255,240,220,.7)}
.cover-right{left:341px;top:0;width:247px;height:330px;background:linear-gradient(180deg,#f2c792,#d79b68 45%,#6b6a6a 80%,#3d3f44)}
.brand{left:55px;top:72px;font-family:Raleway,sans-serif;font-weight:800;font-size:32px;letter-spacing:7px;color:var(--white)}
.brand-sub{left:57px;top:110px;font-family:Raleway,sans-serif;font-size:10px;color:#ddd;letter-spacing:.5px}
.cover-rule{left:50px;top:137px;width:193px;height:2px;background:var(--white)}
.cover-title{left:54px;top:148px;width:200px;font-family:Raleway,sans-serif;font-weight:700;font-size:11.5px;line-height:12px;color:var(--white)}
.cover-by{left:54px;top:184px;font-size:9.5px;color:#bbb}

/* quote */
.s-quote{left:604px;top:9px}
.quote-bg{inset:0;background:linear-gradient(120deg,#5e8fc1,#4677a8 60%,#2f5478)}
.quote-badge{left:261px;top:70px;width:64px;height:64px;border-radius:50%;background:rgba(255,255,255,.35);display:flex;align-items:center;justify-content:center}
.quote-badge div{width:42px;height:42px;border-radius:50%;background:var(--yellow);font:800 26px/46px Raleway,sans-serif;text-align:center;color:#222}
.quote-title{left:0;width:588px;top:150px;font-family:Raleway,sans-serif;font-weight:700;font-size:23px;color:var(--white)}
.quote-body{left:70px;width:448px;top:194px;font-size:9px;line-height:14px;color:#dbe6f2}

/* stats */
.s-stats{left:9px;top:346px}
.stats-bg{left:0;top:0;width:588px;height:238px;background:linear-gradient(160deg,#ececec,#dcdcdc 50%,#e9e9e9)}
.stat{width:250px;text-align:center}
.stat .num{font-size:20px;color:var(--sky);font-weight:400}
.stat .num b{font-weight:700}
.stat .lbl{font-size:10px;color:#222;margin-top:2px}
.stats-div{left:293px;top:105px;width:1px;height:48px;background:#bbb}
.band{left:0;top:238px;width:588px;height:92px;background:var(--navy)}
.band h3{position:absolute;left:32px;top:16px;font-size:10px;font-weight:700;color:var(--white)}
.band p{position:absolute;left:32px;top:36px;width:310px;font-size:6.5px;line-height:10px;color:#d6dce4}

/* failing */
.s-failing{left:604px;top:346px}
.fail-title{left:0;width:588px;top:34px;font-size:24px}
.fail-band{left:0;top:102px;width:588px;height:106px;background:var(--navy)}
.photo-circle{width:88px;height:88px;border-radius:50%;border:2px solid var(--white)}
.num-badge{width:28px;height:26px;border-radius:0 10px 0 10px;font-size:7px;font-weight:700;color:var(--white);display:flex;align-items:center;justify-content:center}
.fail-line{height:2px;width:96px;top:222px}
.fail-quote{width:124px;top:234px;font-size:7.5px;line-height:12px;color:var(--muted);text-align:center}
.fail-quote b{color:#333}

/* problem */
.s-problem{left:9px;top:686px;background:#f5f8fb}
.prob-title{left:0;width:588px;top:30px;font-size:26px}
.tag{height:18px;top:92px;font-size:6.5px;font-weight:700;color:var(--white);text-align:center;line-height:8px;padding:1px 18px 0}
.tag.single{line-height:16px;padding:0}
.arrow{top:92px;width:26px;height:18px;font-size:7px;color:#444;text-align:center;line-height:18px;background:#f0f0f0}
.qmark{left:254px;top:106px;font:800 110px/1 "Source Sans 3",sans-serif;color:var(--sky)}
.cta{left:42px;top:279px;width:504px;height:17px;background:var(--sky);display:flex;align-items:center}
.cta .play{width:93px;height:100%;background:var(--blue);color:var(--white);font-size:7px;display:flex;align-items:center;justify-content:center;flex:none}
.cta span{font-size:6.5px;color:var(--white);padding:0 20px;line-height:8px}

/* results */
.s-results{left:604px;top:686px;background:#f1f1f1}
.results-bg{left:0;top:0;width:588px;height:237px;background:linear-gradient(180deg,#56514a,#7f7768 40%,#4a4640 75%,#2f2d2a)}
.res-title{left:0;width:588px;top:32px;font-size:27px;color:var(--white)}
.res-title b{font-weight:700}
.res-stat{width:200px;text-align:center;top:118px}
.res-stat .num{font-family:Raleway,sans-serif;font-weight:800;font-size:20px;color:var(--yellow)}
.res-stat .lbl{font-size:10px;color:#eee;margin-top:2px}
.res-div{left:293px;top:112px;width:1px;height:50px;background:rgba(255,255,255,.5)}
.clients-h{left:32px;top:246px;font-size:9.5px;font-weight:700;color:#444}
.clients{left:16px;top:263px;width:556px;height:52px;border-radius:26px;background:var(--white);box-shadow:0 1px 4px rgba(0,0,0,.2);display:flex;align-items:center;justify-content:space-around;padding:0 18px}
.clients span{font-size:9px;font-weight:700;color:#333}
</style>
</head>
<body>

<!-- Cover -->
<section class="slide s-cover">
  <div class="abs cover-left" role="img" aria-label="Aerial photo of a city and bridge at dusk"></div>
  <div class="abs cover-band"></div>
  <div class="abs cover-band2"></div>
  <div class="abs cover-right" role="img" aria-label="Aerial photo of a suspension bridge over a river at sunset"></div>
  <div class="abs brand">PONTIVA</div>
  <div class="abs brand-sub">TECHNOLOGY CORPORATION</div>
  <div class="abs cover-rule"></div>
  <div class="abs cover-title">BUILDING THE INTERNET OF INFRASTUCTURE</div>
  <div class="abs cover-by">Presented by: Kurt Milo</div>
  <div class="pill" style="left:49px;top:219px;width:188px">
    <div class="globe"><svg width="11" height="11" viewBox="0 0 12 12" fill="none" stroke="#fff" stroke-width="1"><circle cx="6" cy="6" r="5"/><ellipse cx="6" cy="6" rx="2.2" ry="5"/><path d="M1 6h10"/></svg></div>
    <span>www.pontiva-tech.com</span>
  </div>
</section>

<!-- Quote -->
<section class="slide s-quote">
  <div class="abs quote-bg" role="img" aria-label="Blue-toned photo of a wheelchair wheel on a street"></div>
  <div class="abs quote-badge"><div>“</div></div>
  <div class="abs quote-title center">INFRASTRUCTURE IS F*CKED!</div>
  <p class="abs quote-body center">Quisque commodo lacus sed lectus condimentum cursus. Praesent a diam neque. Aenean ultricies eu orci id euismod. Integer eleifend, lacus quis tincidunt posuere, nisl neque sodales justo, quis suscipit libero odio ut quam. Nam auctor, leo a volutpat rhoncus, erat arcu dignissim velit, in aliquet erat metus quis tellus. Vestibulum nec lobortis augue, at interdum nisl.</p>
</section>

<!-- Stats -->
<section class="slide s-stats">
  <div class="abs stats-bg" role="img" aria-label="Faded photo of cable-stayed bridge"></div>
  <div class="abs stat" style="left:54px;top:105px"><div class="num">¼ of 600,000 <b>BRIDGES</b></div><div class="lbl">Structurally Deficient</div></div>
  <div class="abs stats-div"></div>
  <div class="abs stat" style="left:299px;top:105px"><div class="num">$10T <b>by 2025</b></div><div class="lbl">Cost US &amp; US Businesses</div></div>
  <div class="abs band">
    <h3>PRAESENT MALESUADA TEMPUS SAPIEN</h3>
    <p>Praesent malesuada tempus sapien in consectetur. Nullam eu lobortis nisl. Etiam placerat quis dui non varius. Donec dapibus mi eu eros dictum, congue tempus metus sagittis. Vestibulum lobortis, libero vel gravida pretium, nisi est dapibus quam, sed congue magna est non libero.</p>
  </div>
  <div class="pill" style="left:373px;top:278px;width:174px">
    <div class="globe"><svg width="11" height="11" viewBox="0 0 12 12" fill="none" stroke="#fff" stroke-width="1"><circle cx="6" cy="6" r="5"/><ellipse cx="6" cy="6" rx="2.2" ry="5"/><path d="M1 6h10"/></svg></div>
    <span>www.yoursite.com</span>
  </div>
</section>

<!-- Failing -->
<section class="slide s-failing">
  <div class="abs fail-title head center">Infrastructure in US <b class="underline">is Failing</b></div>
  <div class="abs fail-band"></div>
  <div class="abs photo-circle" style="left:75px;top:114px;background:radial-gradient(#8a8f96,#4f5660)" role="img" aria-label="Aerial photo of a collapsed highway bridge"></div>
  <div class="abs num-badge" style="left:142px;top:110px;background:var(--green)">01</div>
  <div class="abs photo-circle" style="left:243px;top:114px;background:radial-gradient(#c0573a,#4a2a2a)" role="img" aria-label="Photo of firefighters at a warehouse fire"></div>
  <div class="abs num-badge" style="left:310px;top:110px;background:var(--sky)">02</div>
  <div class="abs photo-circle" style="left:410px;top:114px;background:radial-gradient(#b4b4b4,#6c6c6c)" role="img" aria-label="Photo of a pothole in a road"></div>
  <div class="abs num-badge" style="left:477px;top:110px;background:var(--yellow)">03</div>
  <div class="abs fail-line" style="left:72px;background:var(--green)"></div>
  <div class="abs fail-line" style="left:239px;background:var(--sky)"></div>
  <div class="abs fail-line" style="left:406px;background:var(--yellow)"></div>
  <p class="abs fail-quote" style="left:58px">“One in four <b>of the nation’s bridges are rated as</b> structurally deficient” (CivicWorks)</p>
  <p class="abs fail-quote" style="left:225px">“<b>Warehouse where</b> 36 people perished during a fire…<b>not even included in the Bayview Fire Department’s database</b>” (Metro News)</p>
  <p class="abs fail-quote" style="left:392px">“Poorly maintained roads contribute to <b>a third of all highway fatalities</b>. That’s more than <b>13,000 deaths every year</b>.” (Road Watch)</p>
</section>

<!-- Problem -->
<section class="slide s-problem">
  <div class="abs prob-title head center">Why is this <b class="underline">still a problem?</b></div>
  <div class="abs tag single" style="left:53px;width:139px;background:var(--yellow)">TOOLS ARE NON-EXISTANT</div>
  <div class="abs arrow" style="left:192px">▶</div>
  <div class="abs tag" style="left:218px;width:140px;background:var(--sky)">SOLUTIONS OFFERED ARE SILO’D &amp; CONFUSING</div>
  <div class="abs arrow" style="left:358px">▶</div>
  <div class="abs tag single" style="left:384px;width:152px;background:var(--blue)">OFFERINGS ARE STATIC &amp; NON-SCALABLE</div>
  <svg class="abs" style="left:76px;top:126px" width="84" height="84" viewBox="0 0 84 84" role="img" aria-label="Unhappy icon"><circle cx="42" cy="42" r="37" fill="none" stroke="#fbb900" stroke-width="8"/></svg>
  <div class="abs qmark">?</div>
  <svg class="abs" style="left:426px;top:128px" width="86" height="86" viewBox="0 0 86 86" role="img" aria-label="Broken link icon">
    <g fill="none" stroke="#3a6fc4" stroke-width="9" stroke-linecap="round">
      <path d="M36 20 L26 10 a10 10 0 0 0 -14 0 l-4 4 a10 10 0 0 0 0 14 L22 42 a10 10 0 0 0 14 0"/>
      <path d="M50 66 L60 76 a10 10 0 0 0 14 0 l4 -4 a10 10 0 0 0 0 -14 L64 44 a10 10 0 0 0 -14 0"/>
    </g>
    <g stroke="#3a6fc4" stroke-width="3" stroke-linecap="round">
      <path d="M58 10v12M68 18l-8 8M78 30H64"/><path d="M8 56h12M18 68l8-8M28 78V64"/>
    </g>
  </svg>
  <div class="abs cta"><div class="play">▶</div><span>Massive opportunity to disrupt the market with next generation of easy to use, adaptable technologies to streamline &amp; automate infrastructure management!</span></div>
</section>

<!-- Results -->
<section class="slide s-results">
  <div class="abs results-bg" role="img" aria-label="Sepia photo of a suspension bridge over a bay"></div>
  <div class="abs res-title head center">To date, we have <b>saved our clients</b></div>
  <div class="abs res-stat" style="left:70px"><div class="num">$ 3.5 + MM</div><div class="lbl">Lorem ipsum dolor sit amet</div></div>
  <div class="abs res-div"></div>
  <div class="abs res-stat" style="left:316px"><div class="num">10,000+ HOURS</div><div class="lbl">Lorem ipsum dolor sit amet</div></div>
  <div class="abs clients-h">OUR CLIENTS &amp; PARTNERS</div>
  <div class="abs clients">
    <span>Larkspur Airfields</span><span>Routeway</span><span>Aerolink</span><span>Oakmere Capital</span><span>Stratline Engineering</span><span>Fairhaven County</span>
  </div>
</section>

</body>
</html>
```